Flyer Design Project

I require a double sided flyer in PSD format.
The flyer should look fresh and clean.
The flyer is for an digital marketing company that offers various services. The services are broken down into 3 main categories and the design should reflect this.
All the content is provided in the attached file
Industry/Entity Type
Digital
Requirements
Must have
- Front of the leaflet to be mainly white background with appealing text based questions in the colours in large font with relevant images.
Back if the
3 separate boxes using the colours indicated in the attachment for the services on back of the leafet.
Should not have
- Gradients
Borders on the edges of the design
Vignettes
Black elements
Any text below 10pt
Fancy fonts
Do not use old-style fonts

```html
<!DOCTYPE html>
<html lang="en">
<head>
<meta charset="utf-8">
<title>Lumora Internet Marketing Flyer</title>
<link href="https://fonts.googleapis.com/css2?family=Questrial&family=Arimo:wght@700&display=swap" rel="stylesheet">
<style>
  :root {
    --slate: #2f3a48;
    --mist: #e2e2e2;
    --paper: #ffffff;
    --cyan: #45bde3;
    --lime: #9bc43a;
    --sky: #3bb3e0;
    --tangerine: #f08a1f;
    --teal-deep: #345b72;
    --steel: #4e7fa0;
    --white: #ffffff;
  }
  html, body { margin: 0; padding: 0; overflow: hidden; }
  .flyer {
    position: relative;
    width: 846px;
    height: 1200px;
    overflow: hidden;
    background: var(--mist);
    font-family: "Questrial", "Helvetica Neue", Arial, sans-serif;
  }
  .header-band {
    position: absolute; left: 0; top: 0; width: 846px; height: 304px;
    background: var(--slate);
  }
  .footer-band {
    position: absolute; left: 0; top: 1116px; width: 846px; height: 84px;
    background: var(--steel);
  }
  .brand {
    position: absolute; left: 50px; top: 50px;
  }
  .brand-name {
    display: block;
    font-size: 66px; line-height: 1; letter-spacing: 1px;
    color: var(--cyan);
  }
  .brand-tagline {
    display: block; margin-top: 4px; margin-left: 2px;
    font-size: 15px; letter-spacing: 0.5px;
    color: var(--white);
  }
  .call-to-action {
    position: absolute; right: 46px; top: 60px;
    text-align: right; color: var(--white);
    font-size: 32px; line-height: 38px;
  }
  .call-to-action strong { font-family: "Arimo", Arial, sans-serif; font-weight: 700; }
  .call-to-action .free { color: var(--cyan); }
  .accent-bar {
    position: absolute; left: 42px; top: 154px; width: 760px; height: 45px;
    background: var(--cyan);
  }
  .content-panel {
    position: absolute; left: 45px; top: 212px; width: 757px; height: 786px;
    background: var(--paper);
  }
  .word-cloud {
    position: absolute; left: 35px; top: 88px; width: 685px; height: 324px;
    border-radius: 40px;
    background: linear-gradient(100deg, #f4e3e3 0%, #f7eef0 35%, #e9f3e2 60%, #e7eaf4 100%);
  }
  .questions {
    position: absolute; left: 0; top: 470px; width: 757px;
    text-align: center;
    font-family: "Arimo", Arial, sans-serif; font-weight: 700;
    font-size: 31px; line-height: 38px;
    text-shadow: 1px 1px 1px rgba(0,0,0,0.25);
  }
  .questions p { margin: 0; }
  .question-reach { color: var(--lime); }
  .question-found { color: var(--sky); margin-top: 36px !important; }
  .question-growth { color: var(--tangerine); margin-top: 36px !important; }
  .promise-box {
    position: absolute; left: 45px; top: 998px; width: 757px; height: 146px;
    background: var(--teal-deep);
    display: flex; align-items: center; justify-content: center;
  }
  .promise-box p {
    margin: 0 0 16px; color: var(--white);
    font-family: "Arimo", Arial, sans-serif; font-weight: 700; font-size: 27px;
  }
</style>
</head>
<body>
<div class="flyer">
  <div class="header-band"></div>
  <div class="footer-band"></div>

  <div class="brand">
    <span class="brand-name">LUMORA</span>
    <span class="brand-tagline">internet marketing solutions</span>
  </div>

  <div class="call-to-action">
    Call <strong>0121 555 0148</strong><br>
    for a <strong class="free">FREE</strong> Consultation
  </div>

  <div class="accent-bar"></div>

  <main class="content-panel">
    <div class="word-cloud" role="img" aria-label="Colourful word cloud of marketing terms such as social media, website, focus, business, targeted and services"></div>

    <div class="questions">
      <p class="question-reach">Did You Know 85% of Consumers Use The<br>Internet To Find Businesses Like Yours?</p>
      <p class="question-found">Are Your Customers Finding You Online?</p>
      <p class="question-growth">Do You Need More Customers For<br>Your Business?</p>
    </div>
  </main>

  <div class="promise-box">
    <p>Let us help you grow your business online.</p>
  </div>
</div>
</body>
</html>
```